Business Card Design using new attached logo

We are a family run Plumbing and Heating firm looking to improve our company image with an improved business card and new logo.We are looking to keep the company colour (Blue) involved in our design

Reason: New logo added which needs to be incorporated on designs

Industry/Entity Type

Business

Contact Information for Business Card

See attachment of all info required.

Requirements
Must have
• We have just picked a new company logo which is attached.
• Could you please provide your business card designs using this logo.
• We are looking for the logo on the back as well as the front with all the info required

```html
<!DOCTYPE html>
<html lang="en">
<head>
<meta charset="utf-8">
<title>Harlow Plumbing Ltd – Business Cards</title>
<link rel="stylesheet" href="https://fonts.googleapis.com/css2?family=Cinzel:wght@400;600&family=Open+Sans:wght@400;700&display=swap">
<style>
  :root {
    --brand-blue: #1a49c4;
    --brand-blue-dark: #0f36a0;
    --ink: #222428;
    --ink-soft: #3c3f45;
    --card-white: #ffffff;
    --card-grey-light: #f4f4f4;
    --card-grey-dark: #cfcfcf;
    --backdrop: #e4e4e2;
  }
  * { box-sizing: border-box; margin: 0; padding: 0; }
  html, body {
    width: 1200px;
    height: 871px;
    overflow: hidden;
    background: var(--backdrop);
  }
  .canvas {
    position: relative;
    width: 1200px;
    height: 871px;
  }
  .card {
    position: absolute;
    top: 267px;
    width: 540px;
    height: 337px;
    border-radius: 3px;
    box-shadow: 0 10px 24px rgba(0,0,0,0.18);
    overflow: hidden;
  }
  .card--back {
    left: 40px;
    background: linear-gradient(160deg, var(--card-grey-light) 0%, #e6e6e6 55%, var(--card-grey-dark) 100%);
  }
  .card--front {
    left: 620px;
    background: var(--card-white);
  }
  .brand {
    position: absolute;
    display: flex;
    align-items: center;
    gap: 12px;
  }
  .brand__square {
    display: block;
    flex: none;
    background: var(--brand-blue);
  }
  .brand__name {
    font-family: "Cinzel", serif;
    font-weight: 400;
    color: var(--brand-blue);
    letter-spacing: 0.06em;
    white-space: nowrap;
  }
  .card--back .brand {
    left: 50%;
    top: 50%;
    transform: translate(-50%, -50%);
  }
  .card--back .brand__square { width: 52px; height: 52px; }
  .card--back .brand__name { font-size: 25px; }

  .card--front .brand {
    right: 30px;
    top: 40px;
  }
  .card--front .brand__square { width: 52px; height: 52px; }
  .card--front .brand__name { font-size: 23px; }

  .person {
    position: absolute;
    left: 34px;
    top: 120px;
    font-family: "Cinzel", serif;
  }
  .person__name {
    font-size: 19px;
    font-weight: 600;
    color: var(--ink);
    letter-spacing: 0.04em;
  }
  .person__role {
    font-size: 15px;
    color: var(--brand-blue);
    letter-spacing: 0.04em;
  }
  .details {
    position: absolute;
    left: 300px;
    top: 152px;
    font-family: "Open Sans", sans-serif;
    font-style: normal;
    font-size: 11.5px;
    line-height: 1.55;
    color: var(--ink-soft);
  }
  .details__company {
    font-weight: 700;
    color: var(--brand-blue);
    font-size: 11px;
  }
  .contacts {
    list-style: none;
    margin-top: 10px;
  }
  .contacts li {
    display: flex;
    align-items: center;
    gap: 10px;
    height: 19px;
    white-space: nowrap;
  }
  .contacts svg {
    width: 13px;
    height: 13px;
    flex: none;
    fill: var(--brand-blue);
  }
  .card__band {
    position: absolute;
    left: 0;
    right: 0;
    bottom: 0;
    height: 10px;
    background: linear-gradient(90deg, var(--brand-blue), var(--brand-blue-dark));
  }
</style>
</head>
<body>
<main class="canvas">

  <section class="card card--back" aria-label="Card back">
    <div class="brand">
      <span class="brand__square"></span>
      <span class="brand__name">Harlow Plumbing Ltd</span>
    </div>
  </section>

  <section class="card card--front" aria-label="Card front">
    <div class="brand">
      <span class="brand__square"></span>
      <span class="brand__name">Harlow Plumbing Ltd</span>
    </div>

    <div class="person">
      <p class="person__name">Mark Ellison</p>
      <p class="person__role">Director</p>
    </div>

    <address class="details">
      <p class="details__company">HARLOW PLUMBING LTD</p>
      <p>14 Mill Parade</p>
      <p>elm road, sutton, surrey</p>
      <ul class="contacts">
        <li>
          <svg viewBox="0 0 16 16" aria-hidden="true"><path d="M3 2h3l1.5 3.5-2 1.3a8 8 0 0 0 3.7 3.7l1.3-2L14 10v3a1 1 0 0 1-1 1A12 12 0 0 1 2 3a1 1 0 0 1 1-1z"/></svg>
          <span>020 7946 0123</span>
        </li>
        <li>
          <svg viewBox="0 0 16 16" aria-hidden="true"><path d="M4 1h8v4H4zM2 6h12a1 1 0 0 1 1 1v5h-3v3H4v-3H1V7a1 1 0 0 1 1-1zm3 5v3h6v-3z"/></svg>
          <span>020 7946 0456</span>
        </li>
        <li>
          <svg viewBox="0 0 16 16" aria-hidden="true"><path d="M5 1h6a1 1 0 0 1 1 1v12a1 1 0 0 1-1 1H5a1 1 0 0 1-1-1V2a1 1 0 0 1 1-1zm0 2v9h6V3zm3 10a.8.8 0 1 0 0 1.6A.8.8 0 0 0 8 13z"/></svg>
          <span>07700 900123</span>
        </li>
        <li>
          <svg viewBox="0 0 16 16" aria-hidden="true"><path d="M1 3h14v10H1zm1.5 1.2v.3L8 8.6l5.5-4.1v-.3zM2.5 6.2v5.6h11V6.2L8 10.3z"/></svg>
          <span>markellison@harlowplumbing.co.uk</span>
        </li>
      </ul>
    </address>

    <div class="card__band"></div>
  </section>

</main>
</body>
</html>
```